web page layout, style , color, font & flow design

We are developing a single page application. The SPA (single page application) will display natural gas pipeline flow data once the customer logs on. The customer has a choice of the region, the pipeline, the zone on the pipeline, whether the point is a delivery point or receipt point and the state the pipeline flows through.
we have jumpstarted the project and are attaching a pdf of the same.

we are using mockingbird for the wireframe. any designer is free to use this tool to make changes.

A mockingbird wireframe link is added below. you are free to use it and to make changes. please save the changed wireframe in a different name

we are looking for inputs on layout, style , color, font & flow.

A logo jpg file has also been attached.

Target Market(s)

this single web page is going to be used by natural gas traders and schedulers day in and day out. the application is more of business to business corporate application.

Industry/Entity Type

Delivery

Requirements
Must have
• layout ,flow, size, color, font , ease of use.

```html
<!DOCTYPE html>
<html lang="en">
<head>
<meta charset="utf-8">
<title>Gridline Gas Flow Analysis</title>
<link href="https://fonts.googleapis.com/css2?family=Open+Sans:ital,wght@0,400;0,600;0,700;1,600&display=swap" rel="stylesheet">
<style>
:root{
  --page-top:#5a5f64;
  --page-mid:#2c3137;
  --page-bottom:#1f242a;
  --side-bg:#2a2f35;
  --side-menu:#3b444d;
  --side-menu-line:#4a545e;
  --side-sub:#2c3238;
  --side-sub-line:#353c43;
  --side-text:#dde2e6;
  --side-sub-text:#b5bcc3;
  --accent-green:#8cc63f;
  --fly-bg:#48525c;
  --fly-active:#1e2227;
  --panel:#ffffff;
  --panel-edge:#e4e6e8;
  --green:#5ca41c;
  --green-dark:#2f6b0b;
  --orange:#ef8752;
  --blue:#2e8fdc;
  --grid:#dcdcdc;
  --head-bg:#ececec;
  --cell-text:#555a5e;
  --page-btn:#3b434b;
  --page-btn-active:#151719;
  --footer-text:#9aa0a6;
}
*{box-sizing:border-box;margin:0;padding:0}
html,body{width:1200px;height:898px;overflow:hidden}
body{
  font-family:"Open Sans",Arial,sans-serif;
  background:linear-gradient(180deg,var(--page-top) 0%,#4a4f55 18%,var(--page-mid) 55%,var(--page-bottom) 100%);
  position:relative;
}
.sidebar{position:absolute;left:98px;top:0;width:232px;height:850px;background:var(--side-sub)}
.profile{height:96px;background:var(--side-bg);position:relative;border-bottom:1px solid #20252a}
.avatar{position:absolute;left:123px;left:24px;top:18px;width:52px;height:52px;border-radius:50%;background:radial-gradient(circle at 50% 40%,#d9c9b8,#8b7a6c);border:2px solid #e8e8e8}
.welcome{position:absolute;left:84px;top:24px;color:#fff;font-size:14px;line-height:22px}
.welcome .name{display:flex;align-items:center;gap:8px}
.menu-item{height:35px;background:var(--side-menu);border-bottom:1px solid var(--side-menu-line);display:flex;align-items:center;padding:0 0 0 22px;color:var(--side-text);font-size:11.5px;font-weight:600;letter-spacing:.2px;position:relative}
.menu-item svg.icon{width:13px;height:13px;margin-right:10px}
.menu-item .caret{position:absolute;right:14px;top:12px}
.sub-item{height:36px;border-bottom:1px solid var(--side-sub-line);display:flex;align-items:center;padding-left:30px;color:var(--side-sub-text);font-size:12.5px}
.sub-item .lt{margin-right:12px;font-size:13px;color:#9aa2aa}
.sub-item.active{color:var(--accent-green)}
.flyout{position:absolute;left:338px;top:194px;width:156px;background:var(--fly-bg);z-index:5;box-shadow:0 2px 6px rgba(0,0,0,.35)}
.flyout::before{content:"";position:absolute;left:-8px;top:14px;border:8px solid transparent;border-left:0;border-right-color:var(--fly-bg)}
.flyout div{height:30px;line-height:30px;padding-left:13px;color:#fff;font-size:12.5px;border-bottom:1px solid #555f69}
.flyout .on{background:var(--fly-active)}
.panel{position:absolute;left:330px;top:0;width:770px;height:850px;background:var(--panel)}
.panel-edge{position:absolute;left:0;top:46px;width:7px;bottom:0;background:var(--panel-edge)}
.topbar{height:46px;display:flex;align-items:center;padding-left:12px;border-bottom:1px solid #eee}
.brand{display:flex;align-items:center;gap:10px}
.brand-dot{width:30px;height:30px;border-radius:50%;background:var(--blue)}
.brand-name{font-size:13px;font-weight:600;font-style:italic;color:#2b2f33}
.tools{position:absolute;right:20px;top:15px;display:flex;gap:16px}
.tabs{position:absolute;left:7px;top:53px;display:flex;gap:5px}
.tab{width:122px;height:42px;color:#fff;font-size:13px;font-weight:700;display:flex;align-items:center;justify-content:center;letter-spacing:.2px}
.tab.green{background:var(--green)}
.tab.orange{background:var(--orange)}
.tab.blue{background:var(--blue)}
.tab.current{border-top:3px solid var(--green-dark)}
.content-frame{position:absolute;left:7px;top:95px;right:0;bottom:0;border-right:6px solid #f2f2f2}
table.flow{position:absolute;left:36px;top:131px;width:700px;border-collapse:collapse;box-shadow:0 0 0 1px #d2d2d2}
table.flow th,table.flow td{border:1px solid var(--grid);text-align:center;color:var(--cell-text)}
table.flow th{height:52px;background:var(--head-bg);font-weight:400;font-size:12.5px;color:#4a4f53}
table.flow td{height:43px;font-size:11px}
table.flow tbody tr:nth-child(odd) td{background:#fafafa}
.pager{position:absolute;right:33px;top:637px;display:flex;gap:5px;align-items:center}
.pager span{min-width:21px;height:21px;padding:0 4px;background:var(--page-btn);color:#fff;font-size:10.5px;font-weight:600;display:flex;align-items:center;justify-content:center;border-radius:2px}
.pager span.on{background:var(--page-btn-active)}
.pager span.gap{background:none;color:#888;min-width:14px}
.footer{position:absolute;left:0;width:1200px;top:863px;text-align:center;color:var(--footer-text);font-size:11px}
</style>
</head>
<body>

<aside class="sidebar">
  <div class="profile">
    <div class="avatar" role="img" aria-label="User profile photo"></div>
    <div class="welcome">
      <div>Welcome</div>
      <div class="name">Marcus Hale Ro
        <svg width="10" height="7" viewBox="0 0 10 7"><path d="M1 1l4 4 4-4" stroke="#fff" stroke-width="1.6" fill="none"/></svg>
      </div>
    </div>
  </div>
  <div class="menu-item">
    <svg class="icon" viewBox="0 0 14 14"><path d="M13 1L1 6l5 1.5L7.5 13z" fill="#c7ced4"/></svg>LOCATION TYPE
    <svg class="caret" width="7" height="10"><path d="M0 0l7 5-7 5z" fill="#fff"/></svg>
  </div>
  <div class="menu-item">
    <svg class="icon" viewBox="0 0 14 14"><path d="M1 7c2-3.5 10-3.5 12 0-2 3.5-10 3.5-12 0z" fill="#c7ced4"/><circle cx="7" cy="7" r="2" fill="#3b444d"/></svg>STATES
    <svg class="caret" width="7" height="10"><path d="M0 0l7 5-7 5z" fill="#fff"/></svg>
  </div>
  <div class="menu-item">
    <svg class="icon" viewBox="0 0 14 14"><g stroke="#c7ced4" stroke-width="1.4" fill="none"><circle cx="7" cy="2.5" r="1.5"/><path d="M7 4v9M4 6h6M2 9c0 3 10 3 10 0"/></g></svg>ZONES
    <svg class="caret" width="7" height="10"><path d="M0 0l7 5-7 5z" fill="#fff"/></svg>
  </div>
  <div class="menu-item">
    <svg class="icon" viewBox="0 0 14 14"><path d="M11.5 4.5A5 5 0 1 0 12 8" stroke="#c7ced4" stroke-width="1.6" fill="none"/><path d="M12.5 1v4.5H8z" fill="#c7ced4"/></svg>GAS UPDATES
    <svg class="caret" width="7" height="10"><path d="M0 0l7 5-7 5z" fill="#fff"/></svg>
  </div>
  <div class="sub-item active"><span class="lt">&lsaquo;</span>Alderbrook</div>
  <div class="sub-item"><span class="lt">&lsaquo;</span>KRT</div>
  <div class="sub-item"><span class="lt">&lsaquo;</span>Dunmore</div>
  <div class="sub-item"><span class="lt">&lsaquo;</span>Bayside Coast NG</div>
  <div class="sub-item"><span class="lt">&lsaquo;</span>East Ridge NG</div>
  <div class="sub-item"><span class="lt">&lsaquo;</span>Summit Gas</div>
  <div class="sub-item"><span class="lt">&lsaquo;</span>Equiline Inc</div>
  <div class="sub-item"><span class="lt">&lsaquo;</span>Slate Valley Gas</div>
  <div class="sub-item"><span class="lt">&lsaquo;</span>Oakhurst</div>
  <div class="sub-item"><span class="lt">&lsaquo;</span>Harbors &amp; North East</div>
  <div class="sub-item"><span class="lt">&lsaquo;</span>Centenary Pipeline</div>
  <div class="sub-item"><span class="lt">&lsaquo;</span>Federal Fuel Gas Supply Corp</div>
  <div class="sub-item"><span class="lt">&lsaquo;</span>Westport NG</div>
  <div class="sub-item"><span class="lt">&lsaquo;</span>St. Clair River Gas</div>
  <div class="sub-item"><span class="lt">&lsaquo;</span>Cumberland Gas</div>
  <div class="sub-item"><span class="lt">&lsaquo;</span>Tervo</div>
  <div class="sub-item"><span class="lt">&lsaquo;</span>Translo</div>
</aside>

<div class="flyout">
  <div>Timely</div>
  <div class="on">Evening</div>
  <div>Interday1</div>
  <div>Interday2</div>
</div>

<main class="panel">
  <header class="topbar">
    <div class="brand"><span class="brand-dot"></span><span class="brand-name">Gridline Gas Flow Analysis</span></div>
    <div class="tools">
      <svg width="14" height="14" viewBox="0 0 14 14"><path d="M12 5A5.5 5.5 0 0 0 2 5M2 9a5.5 5.5 0 0 0 10 0" stroke="#b5b5b5" stroke-width="1.6" fill="none"/><path d="M12.8 1.5V6H8.5zM1.2 12.5V8h4.3z" fill="#b5b5b5"/></svg>
      <svg width="14" height="14" viewBox="0 0 14 14"><circle cx="6" cy="6" r="4.3" stroke="#b5b5b5" stroke-width="1.8" fill="none"/><path d="M9 9l4 4" stroke="#b5b5b5" stroke-width="2"/></svg>
    </div>
  </header>
  <div class="panel-edge"></div>
  <nav class="tabs">
    <div class="tab green current">NORTHEAST</div>
    <div class="tab orange">MIDWEST</div>
    <div class="tab blue">SOUTHEAST</div>
    <div class="tab green">SOUTHWEST</div>
    <div class="tab orange">CENTRAL</div>
    <div class="tab blue">WEST</div>
  </nav>
  <div class="content-frame"></div>

  <table class="flow">
    <colgroup><col style="width:89px"><col style="width:90px"><col style="width:112px"><col style="width:82px"><col style="width:73px"><col style="width:86px"><col style="width:83px"><col style="width:85px"></colgroup>
    <thead><tr><th>Gasday</th><th>Location</th><th>Location Name</th><th>Flow_Ind</th><th>Loc_Desc</th><th>Op_cap</th><th>Sch_cap</th><th>Op_avail_cap</th></tr></thead>
    <tbody>
      <tr><td>Item 2</td><td>Item 3</td><td>DUNMORE..</td><td>Delivery</td><td>DPQ</td><td>5,47,181</td><td>1,050</td><td>10,500</td></tr>
      <tr><td>Item 4</td><td>Item 2</td><td>COLBURN..</td><td>Delivery</td><td>DPQ</td><td>4,41,824</td><td>805</td><td>4805</td></tr>
      <tr><td>Item 6</td><td>Item 1</td><td>INGLEWO..</td><td>Delivery</td><td>DPQ</td><td>5,402</td><td>402</td><td>4020</td></tr>
      <tr><td>Item 8</td><td>Item 6</td><td>INGLEWO..</td><td>Delivery</td><td>DPQ</td><td>63,989</td><td>3,989</td><td>989</td></tr>
      <tr><td>Item 11</td><td>Item 8</td><td>EQUILINE..</td><td>Delivery</td><td>DPQ</td><td>5,402</td><td>2</td><td>200</td></tr>
      <tr><td>Item 15</td><td>Item 9</td><td>FEDERAL..</td><td>Delivery</td><td>DPQ</td><td>55,588</td><td>788</td><td>88</td></tr>
      <tr><td>Item 17</td><td>Item 10</td><td>FEDERAL..</td><td>Delivery</td><td>DPQ</td><td>24,228</td><td>4,228</td><td>4,228</td></tr>
      <tr><td>Item 15</td><td>Item 9</td><td>FEDERAL..</td><td>Delivery</td><td>DPQ</td><td>55,588</td><td>788</td><td>88</td></tr>
      <tr><td>Item 17</td><td>Item 10</td><td>FEDERAL..</td><td>Delivery</td><td>DPQ</td><td>24,228</td><td>4,228</td><td>4,228</td></tr>
      <tr><td>Item 15</td><td>Item 9</td><td>FEDERAL..</td><td>Delivery</td><td>DPQ</td><td>55,588</td><td>788</td><td>88</td></tr>
    </tbody>
  </table>

  <div class="pager">
    <span>&lsaquo;</span><span>1</span><span class="on">2</span><span>3</span><span>4</span><span>5</span><span class="gap">…</span><span>10</span><span>20</span><span>30</span><span>&rsaquo;</span>
  </div>
</main>

<footer class="footer">© 2014 Gridline Gas Flow Analysis. All Rights Reserved</footer>

</body>
</html>
```